RTV CRAFTED

building services
decks
pergola
renovation
extensions
general building

Target Market(s)

middle to upper class

Industry/Entity Type

building

Contact Information for Business Card

my details 0427839152 pkharlow47@mailvane.net BLD574926

Font styles to use
Serif

Colors
00AB8E
00BBA5
67D7C9
C6EFE9
E9F9F6

Requirements
Must have
• logo on the front and details on the back
Nice to have
• sharp and clean lines

```html
<!DOCTYPE html>
<html lang="en">
<head>
<meta charset="utf-8">
<title>RTV CRAFTED – Business Card</title>
<link href="https://fonts.googleapis.com/css2?family=Roboto+Slab:wght@400;500;700&family=Roboto:wght@400;500&display=swap" rel="stylesheet">
<style>
  :root {
    --canvas: #2a2a2c;
    --teal-deep: #00AB8E;
    --teal: #00BBA5;
    --teal-light: #67D7C9;
    --teal-pale: #C6EFE9;
    --teal-mist: #E9F9F6;
    --card-white: #ffffff;
    --text-grey: #4a4a4a;
    --rule-grey: #6b6b6b;
  }
  * { margin: 0; padding: 0; box-sizing: border-box; }
  html, body {
    width: 1200px; height: 929px; overflow: hidden;
    background: var(--canvas);
    font-family: "Roboto", Arial, sans-serif;
  }
  .sheet { position: relative; width: 1200px; height: 929px; }
  .card {
    position: absolute; left: 250px;
    width: 700px; height: 400px;
    border-radius: 22px;
    overflow: hidden;
  }
  .card--front {
    top: 40px;
    background: radial-gradient(ellipse at 65% 70%, var(--teal) 0%, var(--teal-deep) 75%);
    color: var(--card-white);
  }
  .card--back {
    top: 489px;
    background: var(--card-white);
  }
  .wordmark {
    position: absolute;
    font-family: "Roboto Slab", Georgia, serif;
    font-weight: 700;
    letter-spacing: 1px;
    white-space: nowrap;
    display: flex; align-items: center; gap: 14px;
  }
  .wordmark__square { width: 22px; height: 22px; display: inline-block; }
  .card--front .wordmark {
    left: 0; right: 0; top: 128px; justify-content: center;
    font-size: 56px; color: var(--card-white);
  }
  .card--front .wordmark__square { background: var(--card-white); }
  .services {
    position: absolute; left: 0; right: 0; top: 238px;
    text-align: center; font-size: 19px; line-height: 30px;
    color: var(--teal-mist);
  }
  .services span { margin: 0 7px; }
  .services span::before { content: "•"; margin-right: 5px; }
  .card--back .wordmark {
    right: 48px; top: 46px; font-size: 40px; color: var(--teal-deep);
  }
  .card--back .wordmark__square { background: var(--teal-deep); width: 18px; height: 18px; }
  .divider {
    position: absolute; left: 360px; right: 48px; top: 214px;
    height: 1.5px; background: var(--rule-grey);
  }
  .licence {
    position: absolute; right: 48px; top: 230px;
    font-size: 15px; color: var(--text-grey); letter-spacing: 0.5px;
  }
  .person { position: absolute; left: 48px; top: 196px; }
  .person__name {
    font-family: "Roboto Slab", Georgia, serif;
    font-size: 24px; font-weight: 500; color: var(--teal-deep);
  }
  .person__title { font-size: 19px; color: var(--text-grey); margin-top: 4px; }
  .contact { position: absolute; left: 52px; top: 290px; list-style: none; }
  .contact li {
    display: flex; align-items: center; gap: 10px;
    font-size: 19px; color: var(--text-grey); line-height: 32px;
  }
  .contact svg { width: 18px; height: 18px; fill: var(--teal-deep); }
</style>
</head>
<body>
<main class="sheet">
  <section class="card card--front" aria-label="Card front">
    <div class="wordmark"><span class="wordmark__square"></span>RTV CRAFTED</div>
    <p class="services">
      <span>Building Services</span><span>Decks</span><span>Pergola</span><br>
      <span>Renovation</span><span>Extensions</span><span>General Building</span>
    </p>
  </section>

  <section class="card card--back" aria-label="Card back">
    <div class="wordmark"><span class="wordmark__square"></span>RTV CRAFTED</div>
    <div class="divider"></div>
    <div class="licence">BLD574926</div>
    <div class="person">
      <div class="person__name">Marcus D. Ellery, Esq.</div>
      <div class="person__title">Director &amp; Founder</div>
    </div>
    <ul class="contact">
      <li>
        <svg viewBox="0 0 24 24" aria-hidden="true"><path d="M3 8c0-2 4-4 9-4s9 2 9 4v2h-5V8H8v2H3zM6 11h12l2 9H4zM9 13v2h2v-2zm4 0v2h2v-2zm-4 3v2h2v-2zm4 0v2h2v-2z"/></svg>
        0427839152
      </li>
      <li>
        <svg viewBox="0 0 24 24" aria-hidden="true"><path d="M2 9l10-6 10 6v12H2zm2 1.5V19h16v-8.5l-8 5z"/></svg>
        pkharlow47@mailvane.net
      </li>
    </ul>
  </section>
</main>
</body>
</html>
```